Lantern Holdings Business Card

We are looking to design new business cards for our company. We have two office locations and would like to have both full addresses on the card. Each address needs two lines for the building name and street address and a line or two for the city, state and zip code. There should be a place for 2-3 phone numbers. The addresses and phone numbers are at the bottom of this description. We also need a place to put our company website and one email address. Our logo is attached.
We would like the card to be two sided. The back of the card should have a blue background with some part of our logo design on it. We would like the full logo on the front of the card as well. The front of the card should have a white background with the blue logo. We are open to listing our addresses on the front or the back of the card. The person who designed our logo gave us an excellent business card idea that we really liked. I have attached a picture of his business card idea so that we can build off of it.
Addresses:
The Marlow Exchange
2214 47th Street NW
Washington, DC 20419
Osprey Harbor Tower
815 Tamsin Boulevard #2207
Miami, FL 33987
Phone Numbers: (202) 555-0148
(202) 555-0193
Website: www.lanternholdings-example.com

```html
<!DOCTYPE html>
<html lang="en">
<head>
<meta charset="utf-8">
<title>Lantern Holdings Business Card</title>
<link rel="stylesheet" href="https://fonts.googleapis.com/css2?family=Lato:wght@400;700&display=swap">
<style>
  :root {
    --brand-blue: #2d2f86;
    --brand-blue-light: #5d60b0;
    --rule-blue: #8c8fc4;
    --card-white: #ffffff;
    --backdrop: #e6e7ea;
  }
  * { box-sizing: border-box; margin: 0; padding: 0; }
  html, body { width: 1200px; height: 926px; overflow: hidden; }
  body {
    background: var(--backdrop);
    font-family: "Lato", sans-serif;
    color: var(--brand-blue);
    display: flex;
    flex-direction: column;
    align-items: center;
    justify-content: center;
    gap: 42px;
  }
  .card {
    width: 700px;
    height: 400px;
    background: var(--card-white);
    position: relative;
    overflow: hidden;
    box-shadow: 0 2px 10px rgba(0,0,0,0.12);
  }
  /* Logo card */
  .card--logo { display: flex; align-items: center; justify-content: center; }
  .wordmark { display: flex; align-items: center; gap: 14px; }
  .wordmark__mark { width: 52px; height: 52px; background: var(--brand-blue); border-radius: 6px; flex: none; }
  .wordmark__name {
    font-weight: 400;
    font-size: 50px;
    letter-spacing: 2px;
    text-transform: uppercase;
    color: var(--brand-blue);
    white-space: nowrap;
  }
  /* Contact card */
  .contact-head { padding: 34px 40px 0; }
  .contact-head .wordmark { gap: 10px; }
  .contact-head .wordmark__mark { width: 34px; height: 34px; border-radius: 4px; }
  .contact-head .wordmark__name { font-size: 30px; letter-spacing: 1.5px; }
  .rule { height: 1px; background: var(--rule-blue); }
  .rule--top { margin-top: 22px; }
  .contact-lines { padding: 10px 40px 0; font-size: 17px; font-weight: 700; line-height: 1.35; }
  .contact-line { display: flex; align-items: center; gap: 8px; }
  .contact-line svg { width: 14px; height: 14px; fill: var(--brand-blue); flex: none; }
  .rule--mid { margin-top: 14px; }
  .offices { display: flex; gap: 70px; padding: 22px 40px 0; font-size: 18px; line-height: 1.4; }
  .office { font-style: normal; }
  .office--miami { margin-top: 34px; }
  .office__name { font-weight: 700; }
  .web-band {
    position: absolute; left: 0; right: 0; bottom: 0; height: 64px;
    background: var(--brand-blue);
    color: var(--card-white);
    display: flex; align-items: center;
    padding-left: 40px;
    font-size: 16px; letter-spacing: 3px;
  }
  .band-emblem {
    position: absolute;
    right: 34px;
    bottom: 0;
    width: 120px;
    height: 140px;
    border-radius: 60px 60px 0 0;
    background: linear-gradient(180deg, var(--brand-blue-light) 0%, var(--brand-blue) 100%);
  }
</style>
</head>
<body>
  <section class="card card--logo">
    <div class="wordmark">
      <span class="wordmark__mark"></span>
      <span class="wordmark__name">Lantern Holdings</span>
    </div>
  </section>

  <section class="card card--contact">
    <header class="contact-head">
      <div class="wordmark">
        <span class="wordmark__mark"></span>
        <span class="wordmark__name">Lantern Holdings</span>
      </div>
    </header>
    <div class="rule rule--top"></div>
    <div class="contact-lines">
      <p class="contact-line">
        <svg viewBox="0 0 24 24" aria-hidden="true"><path d="M6.6 10.8a15.1 15.1 0 0 0 6.6 6.6l2.2-2.2c.3-.3.7-.4 1-.2 1.1.4 2.3.6 3.6.6.6 0 1 .4 1 1V20c0 .6-.4 1-1 1C10.6 21 3 13.4 3 4c0-.6.4-1 1-1h3.5c.6 0 1 .4 1 1 0 1.3.2 2.5.6 3.6.1.3 0 .7-.2 1z"/></svg>
        (202) 555-0148 / (202) 555-0193
      </p>
      <p class="contact-line">
        <svg viewBox="0 0 24 24" aria-hidden="true"><path d="M2 5h20v14H2z M2 5l10 8 10-8" /></svg>
        name@lanternholdings-example.com
      </p>
    </div>
    <div class="rule rule--mid"></div>
    <div class="offices">
      <address class="office">
        <p class="office__name">The Marlow Exchange</p>
        <p>2214 47th Street NW</p>
        <p>Washington, DC 20419</p>
      </address>
      <address class="office office--miami">
        <p class="office__name">Osprey Harbor Tower</p>
        <p>815 Tamsin Boulevard #2207</p>
        <p>Miami, FL 33987</p>
      </address>
    </div>
    <footer class="web-band">www.lanternholdings-example.com</footer>
    <div class="band-emblem" role="img" aria-label="Brand emblem graphic from the company logo rising out of the blue band"></div>
  </section>
</body>
</html>
```